KORVO RENEWABLES

New business B2B Energy Renewables website.
Please refer to our competitor https://www.tarnex42.co.uk/ for a similar website.

Need extra days to review

```html
<!DOCTYPE html>
<html lang="en">
<head>
<meta charset="utf-8">
<title>Korvo Renewables</title>
<link rel="stylesheet" href="https://fonts.googleapis.com/css2?family=Montserrat:wght@500;600;700&family=Arimo:wght@400;500&display=swap">
<style>
:root{
  --blue:#1f4fc4;
  --navy:#0b1f33;
  --ink:#222;
  --text:#444;
  --mid:#0e3a8a;
  --dark:#0a2230;
  --white:#fff;
  --line:#d3d6dc;
}
*{margin:0;padding:0;box-sizing:border-box}
html,body{width:1200px;height:3663px;overflow:hidden}
body{position:relative;background:var(--white);font-family:"Arimo",Arial,sans-serif;color:var(--text)}
.abs{position:absolute}
.top-rule{left:0;top:0;width:1200px;height:3px;background:var(--blue)}
.brand{font-family:"Montserrat",Arial,sans-serif;font-weight:700;color:var(--navy);display:flex;align-items:center;gap:10px;white-space:nowrap}
.brand-mark{width:26px;height:26px;background:var(--blue);flex:none}
.header-brand{left:111px;top:50px;font-size:21px;letter-spacing:1px}
.btn{display:flex;align-items:center;justify-content:center;background:var(--blue);color:var(--white);border-radius:30px;font-family:"Montserrat",Arial,sans-serif;font-weight:600;text-transform:uppercase}
.btn-request{left:901px;top:21px;width:187px;height:48px;font-size:15px}
.nav{top:94px;font-family:"Montserrat",Arial,sans-serif;font-weight:500;font-size:14px;color:var(--ink);white-space:nowrap}
.nav.active{color:var(--blue)}
.hero{left:0;top:126px;width:1200px;height:754px}
.hero-photo{position:absolute;inset:0;background:linear-gradient(180deg,#a9adc4 0%,#c4c6d6 25%,#8d99b8 48%,#3d5a8c 62%,#24408a 75%,#1a3580 100%);clip-path:polygon(0 0,100% 0,100% 649px,50% 754px,0 649px)}
.hero-title{left:605px;top:200px;font-family:"Montserrat",Arial,sans-serif;font-weight:700;line-height:1}
.hero-title .l1{display:block;font-size:76px;color:var(--navy)}
.hero-title .l2{display:block;font-size:60px;color:var(--blue);margin-top:10px}
.hero-copy{left:609px;top:360px;font-size:17px;line-height:28px;color:#1c2232;width:520px}
.btn-read{left:611px;top:434px;width:155px;height:55px;font-size:16px}
.dots{left:574px;top:817px;display:flex;gap:7px}
.dots span{width:12px;height:12px;border-radius:50%;background:var(--white)}
.dots span.on{background:var(--blue)}
.sec-title{left:0;width:1200px;text-align:center;font-family:"Montserrat",Arial,sans-serif;font-weight:600;font-size:34px;color:var(--ink)}
.sec-title em{font-style:normal;color:var(--blue)}
.rule{left:579px;width:42px;height:2px;background:var(--blue)}
.svc{width:260px;text-align:center}
.svc h3{font-family:"Montserrat",Arial,sans-serif;font-weight:600;font-size:20px;color:var(--blue);margin-bottom:14px}
.svc h3.dark{color:var(--navy)}
.svc p{font-size:13.5px;line-height:23px;color:var(--text)}
.service-wheel{left:360px;top:1125px;width:480px;height:465px;border-radius:50%;background:radial-gradient(circle at 50% 50%,#ffffff 0%,#ffffff 22%,#2a5bc8 24%,#0e3a8a 55%,#0a2230 100%)}
.about{left:0;top:1663px;width:1200px;height:582px;background:linear-gradient(180deg,#e8ecf2 0%,#f2f4f7 55%,#dfe4ea 70%,#b9c0cc 80%,#5a6a8a 88%,#3b4c70 100%)}
.about-title{left:0;top:1705px;width:1200px;text-align:center;font-family:"Montserrat",Arial,sans-serif;font-size:32px;line-height:41px}
.about-title .a1{color:var(--ink);font-weight:500}
.about-title .a2{color:var(--blue);font-weight:600}
.about-copy{left:225px;top:1822px;width:750px;text-align:center;font-size:13.5px;line-height:27.5px;color:#333}
.btn-learn{left:500px;top:1986px;width:200px;height:60px;font-size:16px}
.card{width:313px;height:408px;background:var(--white);box-shadow:0 0 6px rgba(0,0,0,.18)}
.card .photo{height:242px}
.card h4{font-family:"Montserrat",Arial,sans-serif;font-weight:600;font-size:16px;line-height:23px;color:#333;text-align:center;margin:18px 20px 0;height:46px;display:flex;align-items:center;justify-content:center}
.card p{font-size:13px;line-height:23px;text-align:center;margin:10px 24px 0;color:var(--text)}
.contact{left:0;top:2862px;width:1200px;height:490px;background:linear-gradient(180deg,#ebebeb 0%,#f1f1f1 60%,#e4e4e4 100%)}
.field{background:var(--white);border:1px solid var(--line);font-size:13.5px;color:#444;padding:14px 15px}
.btn-submit{left:515px;top:3235px;width:169px;height:55px;font-size:16px}
.footer{left:0;top:3352px;width:1200px;height:311px;background:var(--blue);color:var(--white)}
.footer-brand{left:153px;top:3443px;font-size:21px;color:var(--white);letter-spacing:1px}
.footer-brand .brand-mark{background:var(--white)}
.vrule{width:1px;height:105px;top:3405px;background:rgba(255,255,255,.35)}
.f-head{font-family:"Montserrat",Arial,sans-serif;font-weight:500;font-size:20px;line-height:24px;color:var(--white)}
.f-text{font-size:12.5px;line-height:23px;color:var(--white);white-space:nowrap}
.hrule{left:111px;top:3580px;width:978px;height:1px;background:rgba(255,255,255,.3)}
.copyright{left:0;top:3610px;width:1200px;text-align:center;font-size:16px;color:var(--white)}
</style>
</head>
<body>

<header>
  <div class="abs top-rule"></div>
  <div class="abs brand header-brand"><span class="brand-mark"></span>KORVO RENEWABLES</div>
  <div class="abs btn btn-request">Get a Request</div>
  <nav>
    <span class="abs nav active" style="left:475px">HOME</span>
    <span class="abs nav" style="left:558px">ABOUT US</span>
    <span class="abs nav" style="left:670px">SERVICES</span>
    <span class="abs nav" style="left:779px">RENEWABLE SOLUTIONS</span>
    <span class="abs nav" style="left:997px">CONTACT US</span>
  </nav>
</header>

<section class="abs hero">
  <div class="hero-photo" role="img" aria-label="Wind turbines on hills at dusk above a field of solar panels"></div>
  <svg class="abs" style="left:0;top:0" width="1200" height="754" viewBox="0 0 1200 754">
    <polyline points="0,649 600,752 1200,649" fill="none" stroke="#1f4fc4" stroke-width="5"/>
  </svg>
</section>
<h1 class="abs hero-title"><span class="l1">KORVO</span><span class="l2">RENEWABLES</span></h1>
<p class="abs hero-copy">Sed ut perspiciatis unde omnis iste natus error sit voluptatem accusantium doloremque laudantium totam</p>
<div class="abs btn btn-read">Read More</div>
<div class="abs dots"><span></span><span class="on"></span><span></span></div>

<section>
  <h2 class="abs sec-title" style="top:933px">OUR <em>SERVICES</em></h2>
  <div class="abs rule" style="top:986px"></div>

  <div class="abs svc" style="left:470px;top:1016px"><h3>MAINTENANCE</h3><p>Sed ut perspiciatis unde omnis iste<br>natus error sit voluptatem</p></div>
  <div class="abs svc" style="left:107px;top:1234px"><h3>CONSULTING</h3><p>Sed ut perspiciatis unde omnis iste<br>natus error sit voluptatem</p></div>
  <div class="abs svc" style="left:839px;top:1287px"><h3 class="dark">INSTALLATION</h3><p>Sed ut perspiciatis unde omnis iste<br>natus error sit voluptatem</p></div>
  <div class="abs svc" style="left:142px;top:1463px"><h3>DESIGN</h3><p>Sed ut perspiciatis unde omnis iste<br>natus error sit voluptatem</p></div>
  <div class="abs svc" style="left:768px;top:1499px"><h3>FINANCE</h3><p>Sed ut perspiciatis unde omnis iste<br>natus error sit voluptatem</p></div>

  <div class="abs service-wheel" role="img" aria-label="Illustrated cycle of five service icons in blue and navy shapes"></div>
</section>

<section>
  <div class="abs about" role="img" aria-label="Bright sky over rows of solar panels at sunrise"></div>
  <h2 class="abs about-title"><span class="a1">ABOUT</span><br><span class="a2">KORVO RENEWABLES</span></h2>
  <div class="abs rule" style="top:1800px"></div>
  <p class="abs about-copy">Sed ut perspiciatis unde omnis iste natus error sit voluptatem accusantium doloremque laudantium, totam rem aperiam, eaque ipsa quae ab illo inventore veritatis et quasi architecto beatae vitae dicta sunt explicabo. Nemo enim ipsam voluptat em quia aut fugit, sed quia consequuntur magni dolores eos qui ratione voluptatem sequi nesciunt. Neque porro quisqua m est, qui dolorem ipsum quia dolor sit amet, consectetur, adipisci velit, sed quia non numquam eius modi tempora inci dunt ut labore et dolore magnam aliquam quaerat voluptatem.</p>
  <div class="abs btn btn-learn">Learn More</div>
</section>

<section>
  <h2 class="abs sec-title" style="top:2302px">RENEWABLE <em>SOLUTIONS</em></h2>
  <div class="abs rule" style="top:2356px"></div>
  <article class="abs card" style="left:111px;top:2388px">
    <div class="photo" role="img" aria-label="Wind turbines and solar panels under a blue sky" style="background:linear-gradient(180deg,#5a8fd6 0%,#9cc0ea 45%,#2c4f9e 70%,#1a3278 100%)"></div>
    <h4>VARIOUS RENEWABLES<br>OFFERED</h4>
    <p>Sed ut perspiciatis unde omnis iste natus error sit voluptatem accusantium dolorem que laudantium totam rem</p>
  </article>
  <article class="abs card" style="left:444px;top:2388px">
    <div class="photo" role="img" aria-label="Light bulb on soil beside coin stacks with young plants" style="background:radial-gradient(circle at 45% 40%,#f4e7a0 0%,#b8a050 30%,#5a5a28 60%,#2e2a16 100%)"></div>
    <h4>ENERGY SAVING<br>ASSESSMENT</h4>
    <p>Sed ut perspiciatis unde omnis iste natus error sit voluptatem accusantium dolorem que laudantium totam rem</p>
  </article>
  <article class="abs card" style="left:775px;top:2388px">
    <div class="photo" role="img" aria-label="Engineer at a desk watching monitoring screens in a control room" style="background:linear-gradient(135deg,#1c2a3c 0%,#3e5a78 45%,#7fa2c2 70%,#22303f 100%)"></div>
    <h4>MONITORING</h4>
    <p>Sed ut perspiciatis unde omnis iste natus error sit voluptatem accusantium dolorem que laudantium totam rem</p>
  </article>
</section>

<section>
  <div class="abs contact" role="img" aria-label="Faded solar panels and turbines in a pale grey backdrop"></div>
  <h2 class="abs sec-title" style="top:2911px">CONTACT <em>US</em></h2>
  <div class="abs rule" style="top:2965px"></div>
  <div class="abs field" style="left:281px;top:2998px;width:311px;height:44px">First Name :</div>
  <div class="abs field" style="left:608px;top:2998px;width:311px;height:44px">Last Name :</div>
  <div class="abs field" style="left:281px;top:3053px;width:311px;height:44px">Email :</div>
  <div class="abs field" style="left:608px;top:3053px;width:311px;height:44px">Phone :</div>
  <div class="abs field" style="left:281px;top:3110px;width:638px;height:104px">Message :</div>
  <div class="abs btn btn-submit">Submit</div>
</section>

<footer>
  <div class="abs footer"></div>
  <div class="abs brand footer-brand"><span class="brand-mark"></span>KORVO RENEWABLES</div>
  <div class="abs vrule" style="left:438px"></div>
  <div class="abs vrule" style="left:768px"></div>

  <svg class="abs" style="left:486px;top:3418px" width="22" height="26" viewBox="0 0 22 26" fill="none" stroke="#fff" stroke-width="1.6"><path d="M11,24 C4,16 3,13 3,10 A8,8 0 0 1 19,10 C19,13 18,16 11,24 Z"/><circle cx="11" cy="10" r="3"/></svg>
  <div class="abs f-head" style="left:526px;top:3418px">ADDRESS</div>
  <div class="abs f-text" style="left:526px;top:3443px">#254 Lorem Ipsum Dummy Lorem<br>Ipsum Dummy Text</div>
  <svg class="abs" style="left:526px;top:3500px" width="44" height="40" viewBox="0 0 44 40"><circle cx="22" cy="20" r="19" fill="none" stroke="#fff" stroke-width="1.8"/></svg>
  <svg class="abs" style="left:578px;top:3500px" width="44" height="40" viewBox="0 0 44 40"><circle cx="22" cy="20" r="19" fill="none" stroke="#fff" stroke-width="1.8"/></svg>

  <svg class="abs" style="left:804px;top:3422px" width="22" height="22" viewBox="0 0 22 22" fill="none" stroke="#fff" stroke-width="1.5"><path d="M4,2 L8,2 L10,7 L7,9 C8,12 10,14 13,15 L15,12 L20,14 L20,18 C20,19 19,20 18,20 C9,20 2,13 2,4 C2,3 3,2 4,2 Z"/></svg>
  <div class="abs f-head" style="left:843px;top:3418px">PHONE</div>
  <div class="abs f-text" style="left:843px;top:3443px">+1 888 888 8888</div>
  <svg class="abs" style="left:806px;top:3494px" width="22" height="16" viewBox="0 0 22 16" fill="none" stroke="#fff" stroke-width="1.5"><rect x="1" y="1" width="20" height="14"/><path d="M1,1 L11,9 L21,1"/></svg>
  <div class="abs f-head" style="left:845px;top:3487px">EMAIL</div>
  <div class="abs f-text" style="left:845px;top:3512px">info@companyname.com</div>

  <div class="abs hrule"></div>
  <div class="abs copyright">© 2022 Korvo Renewables.All rights reserved.</div>
</footer>

</body>
</html>
```